Business Card Design For DJ Company

I'm rebranding my wedding and event dj company. I am looking for a modern, luxury, & fun design to match my new logo and website design. Please see attached logo and new webpage design. Colors should match. Design should flow with logo and website for recognition. I want to attract young adults. I plan on printing metallic finish cards so please keep hat in mind.

Target Market(s)

Millennials

Contact Information for Business Card

Name: Dario Velloza
Company: Coral Tide Fiesta DJ
Services: DJ – Photo Booth – Event Lighting – LED Robot

Website: www.coraltidefiestadj.example
Email: dario@coraltidefiestadj.example
Phone: (555)014-7392

Instagram: @ctfiestadj
Facebook: @ctfiestadj
Twitter - @ctfiestadj

Se Habla Español

Font styles to use
Serif
Sans Serif

Colors

Designer to choose colors to be used in the design.

Requirements
Nice to have
• Transparent Gradient background - Image related to weddings

```html
<!DOCTYPE html>
<html lang="en">
<head>
<meta charset="utf-8">
<title>Coral Tide Fiesta DJ – Business Card</title>
<link rel="stylesheet" href="https://fonts.googleapis.com/css2?family=Open+Sans:wght@400;700&display=swap">
<style>
  :root {
    --page-bg: #f2f2f2;
    --card-dark: #333333;
    --card-light: #ffffff;
    --ink: #222222;
    --ink-soft: #8a8a8a;
    --orange: #f7941d;
    --green: #7ac143;
    --sky: #29a8e0;
    --purple: #92278f;
    --navy: #2e3192;
    --light-blue: #58a9de;
    --white: #ffffff;
  }
  * { box-sizing: border-box; margin: 0; padding: 0; }
  html, body { width: 1200px; height: 1200px; overflow: hidden; }
  body {
    background: var(--page-bg);
    font-family: "Open Sans", Arial, sans-serif;
    display: flex;
    flex-direction: column;
    align-items: center;
    justify-content: center;
    gap: 56px;
  }
  .card {
    position: relative;
    width: 900px;
    height: 514px;
    overflow: hidden;
    box-shadow: 0 10px 30px rgba(0,0,0,0.15);
  }

  /* Back side */
  .card--back { background: var(--card-dark); color: var(--white); }
  .brand-mark {
    position: absolute;
    display: flex;
    align-items: center;
    gap: 14px;
  }
  .brand-mark__dot {
    width: 30px; height: 30px;
    border-radius: 50%;
    background: var(--orange);
    flex: none;
  }
  .brand-mark__name {
    font-weight: 700;
    font-size: 34px;
    color: var(--orange);
    white-space: nowrap;
  }
  .card--back .brand-mark { left: 50%; top: 170px; transform: translateX(-50%); }
  .social-row {
    position: absolute;
    left: 0; right: 0; bottom: 44px;
    display: flex;
    justify-content: space-around;
    padding: 0 60px;
  }
  .social-handle {
    display: flex; align-items: center; gap: 12px;
    font-size: 24px;
  }
  .social-handle__icon {
    width: 24px; height: 24px;
    border: 2px solid var(--white);
    border-radius: 4px;
  }
  .stripe {
    position: absolute; left: 0; right: 0; bottom: 0;
    height: 8px; display: flex;
  }
  .stripe span { flex: 1; }
  .stripe .s1 { background: var(--purple); }
  .stripe .s2 { background: var(--navy); }
  .stripe .s3 { background: var(--light-blue); }

  /* Front side */
  .card--front { background: var(--card-light); color: var(--ink); }
  .card--front .brand-mark { left: 48px; top: 230px; }
  .card--front .brand-mark__name { font-size: 30px; }
  .details {
    position: absolute;
    left: 470px; top: 70px;
  }
  .details__name { font-size: 36px; font-weight: 700; line-height: 1.1; }
  .details__role { font-size: 24px; color: var(--ink-soft); margin-top: 2px; }
  .contact { list-style: none; margin-top: 30px; }
  .contact li {
    display: flex; align-items: center; gap: 12px;
    font-size: 22px; line-height: 1.4;
  }
  .contact svg { width: 18px; height: 18px; flex: none; }
  .company {
    position: absolute;
    left: 470px; top: 370px;
  }
  .company__name { font-size: 24px; font-weight: 700; }
  .company__services { font-size: 22px; margin-top: 2px; }
  .band {
    position: absolute; left: 0; right: 0; bottom: 0;
    height: 22px; background: var(--orange);
  }
</style>
</head>
<body>

<section class="card card--back">
  <div class="brand-mark">
    <span class="brand-mark__dot"></span>
    <span class="brand-mark__name">Coral Tide Fiesta DJ</span>
  </div>
  <div class="social-row">
    <div class="social-handle"><span class="social-handle__icon"></span>@ctfiestadj</div>
    <div class="social-handle"><span class="social-handle__icon"></span>@ctfiestadj</div>
    <div class="social-handle"><span class="social-handle__icon"></span>@ctfiestadj</div>
  </div>
  <div class="stripe"><span class="s1"></span><span class="s2"></span><span class="s3"></span></div>
</section>

<section class="card card--front">
  <div class="brand-mark">
    <span class="brand-mark__dot"></span>
    <span class="brand-mark__name">Coral Tide Fiesta DJ</span>
  </div>
  <div class="details">
    <div class="details__name">Dario Velloza</div>
    <div class="details__role">Position Here</div>
    <ul class="contact">
      <li>
        <svg viewBox="0 0 20 20"><path d="M5 2 L8 6 L6 8 Q8 12 12 14 L14 12 L18 15 L16 18 Q8 18 3 10 Q2 5 5 2 Z" fill="#29a8e0"/></svg>
        (555) 014-7392
      </li>
      <li>
        <svg viewBox="0 0 20 20"><rect x="2" y="5" width="16" height="11" fill="none" stroke="#29a8e0" stroke-width="2"/><path d="M2 5 L10 11 L18 5" fill="none" stroke="#29a8e0" stroke-width="2"/></svg>
        dario@coraltidefiestadj.example
      </li>
      <li>
        <svg viewBox="0 0 20 20"><circle cx="10" cy="10" r="8" fill="none" stroke="#29a8e0" stroke-width="1.6"/><ellipse cx="10" cy="10" rx="3.5" ry="8" fill="none" stroke="#29a8e0" stroke-width="1.4"/><path d="M2 10 H18" stroke="#29a8e0" stroke-width="1.4"/></svg>
        www.coraltidefiestadj.example
      </li>
    </ul>
  </div>
  <div class="company">
    <div class="company__name">Coral Tide Fiesta DJ</div>
    <div class="company__services">DJ • Photo Booth • Event Lighting • LED Robot</div>
  </div>
  <div class="band"></div>
</section>

</body>
</html>
```